Book Cover

Book cover for a study guide on Galatians. The title would be: "Unbound Hearts: Called Out to Walk Open" Possibly using a bird breaking free from a cage.+

Target Market(s)

We will sell them to our church.

Requirements
Must have
• Authors are Dr. Martin Oskerby and Dr. Helen Oskerby

```html
<!DOCTYPE html>
<html lang="en">
<head>
<meta charset="utf-8">
<title>Unbound Hearts: Called Out to Walk Open — Book Cover</title>
<link rel="stylesheet" href="https://fonts.googleapis.com/css2?family=Cinzel+Decorative:wght@700;900&family=Libre+Caslon+Text:wght@400;700&display=swap">
<style>
  :root {
    --leather-light: #8e5e39;
    --leather-mid: #6a3f22;
    --leather-dark: #3d1c0d;
    --ink-light: #f4ece6;
    --ink-soft: #d8c2b8;
    --title-shade: #c9b8b2;
    --title-depth: #4a2414;
    --ornament-tone: rgba(224, 200, 190, 0.28);
  }
  html, body {
    margin: 0;
    padding: 0;
    width: 883px;
    height: 1200px;
    overflow: hidden;
    background: var(--leather-dark);
  }
  .cover {
    position: relative;
    width: 883px;
    height: 1200px;
    overflow: hidden;
    background: radial-gradient(ellipse 70% 60% at 50% 42%, var(--leather-light) 0%, var(--leather-mid) 55%, var(--leather-dark) 100%);
    font-family: "Libre Caslon Text", Georgia, serif;
    color: var(--ink-light);
  }
  .frame-line {
    position: absolute;
    background: var(--ink-soft);
  }
  .frame-line--top { top: 57px; left: 220px; width: 400px; height: 1.5px; }
  .frame-line--bottom { top: 1133px; left: 220px; width: 446px; height: 1.5px; }
  .frame-line--left { top: 250px; left: 60px; width: 1.5px; height: 697px; }
  .frame-line--right { top: 250px; left: 822px; width: 1.5px; height: 697px; }

  .corner-ornament {
    position: absolute;
    width: 190px;
    height: 190px;
    background: var(--ornament-tone);
    border-radius: 6px;
  }
  .corner-ornament--tl { top: 48px; left: 50px; }
  .corner-ornament--tr { top: 48px; right: 50px; }
  .corner-ornament--bl { bottom: 48px; left: 50px; }
  .corner-ornament--br { bottom: 48px; right: 50px; }

  .emblem {
    position: absolute;
    left: 350px;
    top: 200px;
    width: 180px;
    height: 175px;
    border-radius: 50%;
    background: radial-gradient(circle, rgba(244,236,230,0.35) 0%, rgba(244,236,230,0.15) 70%);
  }

  .title {
    position: absolute;
    left: 0;
    top: 478px;
    width: 883px;
    margin: 0;
    text-align: center;
    font-family: "Cinzel Decorative", "Times New Roman", serif;
    font-weight: 900;
    font-size: 66px;
    line-height: 1.1;
    letter-spacing: 1px;
    background: linear-gradient(180deg, var(--ink-light) 0%, var(--ink-light) 55%, var(--title-shade) 56%, var(--title-shade) 100%);
    -webkit-background-clip: text;
    background-clip: text;
    color: transparent;
    filter: drop-shadow(4px 4px 0 var(--title-depth));
  }
  .title-rule {
    position: absolute;
    left: 205px;
    top: 641px;
    width: 485px;
    height: 1.5px;
    background: var(--ink-soft);
  }
  .subtitle {
    position: absolute;
    left: 0;
    top: 652px;
    width: 883px;
    margin: 0;
    text-align: center;
    font-weight: 700;
    font-size: 19px;
    letter-spacing: 3px;
    color: var(--ink-light);
  }

  .authors-heading {
    position: absolute;
    left: 0;
    top: 890px;
    width: 883px;
    margin: 0;
    text-align: center;
    font-weight: 700;
    font-size: 28px;
    letter-spacing: 2px;
  }
  .authors-rule {
    position: absolute;
    left: 300px;
    top: 935px;
    width: 306px;
    height: 2px;
    background: var(--ink-light);
  }
  .author-list {
    position: absolute;
    left: 318px;
    top: 966px;
    margin: 0;
    padding: 0;
    list-style: none;
    font-weight: 700;
    font-size: 16px;
    letter-spacing: 0.5px;
  }
  .author {
    display: flex;
    align-items: center;
    height: 26px;
  }
  .author svg { margin-right: 14px; }
  .author-joiner {
    height: 20px;
    padding-left: 54px;
    font-size: 10px;
    line-height: 20px;
    letter-spacing: 1px;
  }
</style>
</head>
<body>
  <main class="cover">
    <div class="frame-line frame-line--top"></div>
    <div class="frame-line frame-line--bottom"></div>
    <div class="frame-line frame-line--left"></div>
    <div class="frame-line frame-line--right"></div>

    <div class="corner-ornament corner-ornament--tl" role="img" aria-label="Decorative floral corner flourish"></div>
    <div class="corner-ornament corner-ornament--tr" role="img" aria-label="Decorative floral corner flourish"></div>
    <div class="corner-ornament corner-ornament--bl" role="img" aria-label="Decorative floral corner flourish"></div>
    <div class="corner-ornament corner-ornament--br" role="img" aria-label="Decorative floral corner flourish"></div>

    <div class="emblem" role="img" aria-label="Illustration of a bird flying free from an open hanging birdcage inside a circle"></div>

    <h1 class="title">UNBOUND HEARTS</h1>
    <div class="title-rule"></div>
    <p class="subtitle">CALLED OUT TO WALK OPEN</p>

    <h2 class="authors-heading">AUTHORS ARE</h2>
    <div class="authors-rule"></div>
    <ul class="author-list">
      <li class="author">
        <svg width="9" height="11" viewBox="0 0 9 11" aria-hidden="true"><path d="M0 0 L9 5.5 L0 11 Z" fill="#f4ece6"/></svg>
        Dr. MARTIN OSKERBY
      </li>
      <li class="author-joiner">AND</li>
      <li class="author">
        <svg width="9" height="11" viewBox="0 0 9 11" aria-hidden="true"><path d="M0 0 L9 5.5 L0 11 Z" fill="#f4ece6"/></svg>
        Dr. HELEN OSKERBY
      </li>
    </ul>
  </main>
</body>
</html>
```